New Web Design Project

Require a website for The Marrow Orchard. All relevant information is in the uploaded files.

website to be responsive to work on mobile.

Required in html5, css

Coding

Coded - Design and coding required

Number of Pages Required

3 page

```html
<!DOCTYPE html>
<html lang="en">
<head>
<meta charset="utf-8">
<title>The Marrow Orchard Company</title>
<link href="https://fonts.googleapis.com/css2?family=Poppins:wght@400;500;600;700&display=swap" rel="stylesheet">
<style>
:root{
  --orange:#f7941d;
  --orange-soft:#f9a440;
  --orange-btn:#f3861d;
  --green:#7dc242;
  --green-deep:#6fb237;
  --ink:#3b3b3b;
  --text:#555;
  --muted:#8a8a8a;
  --hero-a:#e3efd8;
  --hero-b:#eef6e6;
  --paper:#f7f7f7;
  --dark:#2f2f2f;
}
*{box-sizing:border-box;margin:0;padding:0}
html,body{width:1200px;height:3199px;overflow:hidden}
body{position:relative;font-family:'Poppins',sans-serif;color:var(--text);background:#fff}
.abs{position:absolute}

/* header */
.site-header{position:absolute;left:0;top:0;width:1200px;height:97px;background:#fff;border-bottom:1px solid #e6e6e6;z-index:5}
.brand{position:absolute;left:88px;top:33px;display:flex;align-items:center;gap:9px;font-size:19px;line-height:30px;font-weight:700;color:var(--ink);white-space:nowrap}
.brand-dot{width:28px;height:28px;border-radius:50%;background:var(--orange);flex:none}
.main-nav{position:absolute;left:376px;top:41px;display:flex;font-size:13px;color:var(--ink)}
.main-nav a{color:inherit;text-decoration:none;margin-right:33px}
.header-divider{position:absolute;left:828px;top:0;width:1px;height:97px;background:#e6e6e6}
.account{position:absolute;left:855px;top:41px;font-size:14px;font-weight:500;color:var(--ink)}
.btn-login{position:absolute;left:1002px;top:28px;width:108px;height:44px;border-radius:22px;background:var(--green);box-shadow:0 3px 0 var(--green-deep);color:#fff;font-size:14px;font-weight:600;display:flex;align-items:center;justify-content:center;gap:6px}

/* hero */
.hero{position:absolute;left:0;top:97px;width:1200px;height:640px;background:linear-gradient(135deg,var(--hero-a),var(--hero-b) 55%,#e6f0dc)}
.hero-title{position:absolute;left:0;width:1200px;top:205px;text-align:center;font-size:44px;line-height:53px;font-weight:600;color:var(--ink);z-index:2}
.hero-sub{position:absolute;left:0;width:1200px;top:329px;text-align:center;font-size:14px;font-weight:600;color:var(--ink);z-index:2}
.btn-orange{position:absolute;left:519px;top:367px;width:162px;height:48px;border-radius:24px;background:var(--orange-btn);box-shadow:0 4px 0 #d97214;color:#fff;font-size:15px;font-weight:600;display:flex;align-items:center;justify-content:center;z-index:2}
.produce{position:absolute;border-radius:50%}

/* about */
.about-title{position:absolute;left:88px;top:878px;font-size:50px;font-weight:700;color:var(--ink)}
.about-rule{position:absolute;left:90px;top:964px;width:62px;height:3px;background:var(--ink)}
.about-copy{position:absolute;left:166px;top:955px;width:455px;font-size:14px;line-height:22px;color:var(--text)}
.about-copy p{margin-bottom:19px}
.about-art{position:absolute;left:688px;top:833px;width:424px;height:525px;border-radius:48% 48% 50% 50%;background:radial-gradient(circle at 55% 60%,#f68b2a,#f4a63a 45%,#b7d63b 80%,#8cc43a)}
.salad-art{position:absolute;left:0;top:1318px;width:118px;height:130px;border-radius:0 60% 40% 0;background:linear-gradient(135deg,#e2564a,#7db84a)}

/* people */
.section-title-light{position:absolute;left:0;width:1200px;top:1585px;text-align:center;font-size:48px;font-weight:700;color:#fff}
.rule-light{position:absolute;left:570px;top:1669px;width:60px;height:3px;background:#fff}
.person{position:absolute;top:1700px;width:212px;height:211px;background:var(--orange-soft);color:#fff;padding:36px 0 0 36px}
.person h3{font-size:22px;line-height:26px;font-weight:700}
.person .role{font-size:12px;margin-top:12px;font-weight:500}
.person .link{position:absolute;left:36px;top:154px;display:flex;align-items:center;gap:10px;font-size:11px;font-weight:600}
.person .link i{width:24px;height:24px;border-radius:50%;background:#fff}
.portrait{position:absolute;top:1700px;width:212px;height:211px;background:linear-gradient(160deg,#e4e4e4,#b9b9b9 60%,#3a3a3a)}

/* contact */
.contact-card{position:absolute;left:206px;top:2053px;width:826px;height:439px;background:#fff;box-shadow:0 20px 50px rgba(0,0,0,.1)}
.frame{position:absolute;border:1px solid #9a9a9a}
.contact-title{position:absolute;left:206px;width:826px;top:2118px;text-align:center;font-size:52px;font-weight:600;color:var(--ink)}
.rule-dark{position:absolute;left:570px;top:2192px;width:60px;height:3px;background:var(--ink)}
.field{position:absolute;width:183px;height:14px;border:2px solid #444;border-top:0}
.label{position:absolute;font-size:11px;color:var(--ink);font-weight:500}
.message-box{position:absolute;left:335px;top:2308px;width:566px;height:49px;border:2px solid #444;border-top:0}
.btn-green{position:absolute;left:519px;top:2391px;width:162px;height:48px;border-radius:24px;background:var(--green);box-shadow:0 4px 0 var(--green-deep);color:#fff;font-size:15px;font-weight:600;display:flex;align-items:center;justify-content:center}

/* faq */
.faq{position:absolute;left:233px;top:2650px;width:735px;height:167px;border-radius:14px;background:var(--green);overflow:hidden;color:#fff}
.faq-tab{position:absolute;left:0;top:0;width:420px;height:167px;background:#89c944;clip-path:polygon(0 0,86% 0,100% 20%,100% 100%,0 100%)}
.faq-small{position:absolute;left:47px;top:55px;font-size:18px;font-weight:500}
.faq-big{position:absolute;left:47px;top:82px;font-size:40px;font-weight:600;white-space:nowrap}

/* footer */
.foot-brand{position:absolute;left:87px;top:2945px;width:240px;display:flex;align-items:center;gap:12px;font-size:30px;line-height:36px;font-weight:700;color:var(--ink)}
.foot-brand span{width:34px;height:34px;border-radius:50%;background:var(--orange);flex:none}
.foot-divider{position:absolute;top:2890px;width:1px;height:190px;background:#e3e3e3}
.foot-links{position:absolute;left:420px;top:2908px;list-style:none;font-size:14px;line-height:31px;color:var(--ink)}
.foot-links li::before{content:"›";color:#bbb;font-size:11px;margin-right:6px}
.social{position:absolute;left:677px;top:2910px;list-style:none;font-size:14px;line-height:30px;color:var(--ink)}
.social li{display:flex;align-items:center;gap:7px}
.social i{width:24px;height:24px;border-radius:50%;background:#3b5aa0}
.store{position:absolute;left:894px;width:177px;height:48px;border-radius:24px;background:var(--dark);color:#fff;padding:8px 0 0 56px}
.store small{display:block;font-size:7px;line-height:9px}
.store b{font-size:16px;font-weight:600;line-height:20px}
.chat{position:absolute;left:1127px;top:3060px;width:60px;height:60px;border-radius:50%;background:var(--orange)}
.to-top{position:absolute;left:1138px;top:3126px;width:38px;height:38px;border-radius:50%;background:#333}
.foot-rule{position:absolute;left:88px;top:3148px;width:1024px;height:1px;background:#e3e3e3}
.copyright{position:absolute;left:0;width:1200px;top:3166px;text-align:center;font-size:13px;color:var(--ink)}
</style>
</head>
<body>

<header class="site-header">
  <div class="brand"><span class="brand-dot"></span>The Marrow Orchard</div>
  <nav class="main-nav">
    <a href="#">HOME</a><a href="#">ABOUT US</a><a href="#">PRODUCE</a><a href="#">PEOPLE</a><a href="#">CONTACT US</a>
  </nav>
  <div class="header-divider"></div>
  <div class="account">Have an account?</div>
  <div class="btn-login">
    <svg width="11" height="12" viewBox="0 0 11 12"><circle cx="5.5" cy="3" r="3" fill="#fff"/><path d="M0 12c0-4 2.5-5.5 5.5-5.5S11 8 11 12z" fill="#fff"/></svg>LOG IN
  </div>
</header>

<section class="hero">
  <div class="produce" role="img" aria-label="Tomato" style="left:0;top:88px;width:90px;height:90px;background:radial-gradient(circle at 40% 35%,#f25a4a,#c81e1e)"></div>
  <div class="produce" role="img" aria-label="Green chili" style="left:230px;top:5px;width:100px;height:140px;border-radius:50% 10%;background:linear-gradient(135deg,#9bcf3e,#4c8f1f)"></div>
  <div class="produce" role="img" aria-label="Basil leaf" style="left:545px;top:0;width:105px;height:58px;background:linear-gradient(135deg,#7dbb3f,#3f7f1f)"></div>
  <div class="produce" role="img" aria-label="Orange slice" style="left:1085px;top:0;width:80px;height:48px;background:linear-gradient(#fbc34a,#f18a1c)"></div>
  <div class="produce" role="img" aria-label="Yellow pepper" style="left:35px;top:250px;width:145px;height:155px;border-radius:45%;background:radial-gradient(circle at 40% 40%,#ffd543,#eca20e)"></div>
  <div class="produce" role="img" aria-label="Broccoli" style="left:945px;top:125px;width:215px;height:200px;background:radial-gradient(circle at 50% 40%,#6fb23a,#2e6b1a)"></div>
  <div class="produce" role="img" aria-label="Yellow pepper" style="left:740px;top:400px;width:72px;height:72px;background:radial-gradient(#ffd543,#eca20e)"></div>
  <div class="produce" role="img" aria-label="Green chili" style="left:775px;top:375px;width:200px;height:180px;border-radius:10% 60%;background:linear-gradient(45deg,#4c8f1f,#9bcf3e);opacity:.85"></div>
  <div class="produce" role="img" aria-label="Orange slice" style="left:228px;top:470px;width:118px;height:70px;background:linear-gradient(#fbc34a,#f18a1c)"></div>
  <div class="produce" role="img" aria-label="Broccoli" style="left:120px;top:520px;width:145px;height:120px;border-radius:50% 50% 0 0;background:radial-gradient(circle at 50% 40%,#6fb23a,#2e6b1a)"></div>
  <div class="produce" role="img" aria-label="Tomato" style="left:520px;top:530px;width:140px;height:110px;border-radius:50% 50% 0 0;background:radial-gradient(circle at 40% 35%,#f25a4a,#c81e1e)"></div>
  <div class="produce" role="img" aria-label="Tomato" style="left:1140px;top:520px;width:60px;height:60px;background:radial-gradient(circle at 40% 35%,#f25a4a,#c81e1e)"></div>
  <h1 class="hero-title">The Marrow Orchard Company<br>was incorporated</h1>
  <div class="hero-sub">UP TO 30% OFF ON ALL PRODUCTS</div>
  <div class="btn-orange">CONTACT US</div>
</section>

<section class="about">
  <h2 class="about-title">About Us</h2>
  <div class="about-rule"></div>
  <div class="about-copy">
    <p>The Marrow Orchard Company was incorporated with the objective of introducing new vendors to the Canadian market through a trusted and mutual business relation</p>
    <p>It was set up by Dario Menzel and Niko Pallas who have a combined experience of over 45 years in the fresh produce business. With Dario's expertise in global sourcing and Niko's vast connection and know how of the Canadian market, we have helped our existing partners grow and expand their reach in the Canadian fresh produce market.</p>
    <p>Our expertise and supply chain knowledge allow us to develop programs and introduce new products to the Canadian consumer, via retail and wholesale channels across Canada.</p>
    <p>Get in touch to discuss how we can add value to your business</p>
  </div>
  <div class="about-art" role="img" aria-label="Citrus fruit and kiwi collage"></div>
  <div class="salad-art" role="img" aria-label="Fresh salad vegetables"></div>
</section>

<svg class="abs" style="left:0;top:1420px" width="1200" height="900" viewBox="0 0 1200 900">
  <path d="M0 20 C300 -10 560 100 860 140 C1000 160 1120 110 1200 90 L1200 720 C1100 730 980 760 820 760 L0 920 Z" fill="var(--orange)"/>
  <path d="M0 18 C300 -14 560 94 860 133 C1000 152 1120 105 1200 92 L1200 96 C1120 118 1000 166 860 148 C560 108 300 2 0 26 Z" fill="var(--green)"/>
  <path d="M820 610 C920 560 1050 540 1200 535 L1200 720 C1100 720 980 700 820 640 Z" fill="var(--green)"/>
  <path d="M0 860 C300 800 600 780 1200 680 L1200 900 L0 900 Z" fill="var(--paper)"/>
</svg>
<div class="abs" style="left:0;top:2300px;width:1200px;height:899px;background:var(--paper)"></div>
<svg class="abs" style="left:0;top:2250px" width="1200" height="120" viewBox="0 0 1200 120"><path d="M0 60 C300 10 600 0 1200 -40 L1200 0 L0 0 Z" fill="var(--orange)"/></svg>

<h2 class="section-title-light">People</h2>
<div class="rule-light"></div>
<div class="person" style="left:177px">
  <h3>Dario<br>Menzel</h3>
  <div class="role">Founder &amp; President</div>
  <div class="link"><i></i>WORKLINE</div>
</div>
<div class="portrait" style="left:388px" role="img" aria-label="Portrait of Dario Menzel"></div>
<div class="person" style="left:600px">
  <h3>Niko<br>Pallas</h3>
  <div class="role">Founder</div>
  <div class="link"><i></i>WORKLINE</div>
</div>
<div class="portrait" style="left:812px" role="img" aria-label="Portrait of Niko Pallas"></div>

<div class="contact-card"></div>
<div class="frame" style="left:235px;top:2082px;width:192px;height:0;border-width:1px 0 0 0"></div>
<div class="frame" style="left:812px;top:2082px;width:192px;height:0;border-width:1px 0 0 0"></div>
<div class="frame" style="left:235px;top:2082px;width:0;height:382px;border-width:0 0 0 1px"></div>
<div class="frame" style="left:1003px;top:2082px;width:0;height:140px;border-width:0 0 0 1px"></div>
<div class="frame" style="left:1003px;top:2332px;width:0;height:132px;border-width:0 0 0 1px"></div>
<div class="frame" style="left:235px;top:2464px;width:192px;height:0;border-width:1px 0 0 0"></div>
<div class="frame" style="left:812px;top:2464px;width:192px;height:0;border-width:1px 0 0 0"></div>
<h2 class="contact-title">Contact Us</h2>
<div class="rule-dark"></div>
<div class="label" style="left:348px;top:2230px">NAME</div>
<div class="label" style="left:539px;top:2230px">EMAIL</div>
<div class="label" style="left:730px;top:2230px">PHONE</div>
<div class="field" style="left:335px;top:2248px"></div>
<div class="field" style="left:526px;top:2248px"></div>
<div class="field" style="left:717px;top:2248px"></div>
<div class="label" style="left:348px;top:2292px">MESSAGE</div>
<div class="message-box"></div>
<div class="btn-green">SUBSCRIBE</div>
<div class="produce" role="img" aria-label="Tomato with water drops" style="left:120px;top:2160px;width:185px;height:185px;background:radial-gradient(circle at 40% 35%,#f4675a,#c01717 70%)"></div>
<div class="produce" role="img" aria-label="Yellow bell pepper" style="left:915px;top:2385px;width:165px;height:155px;border-radius:45%;background:radial-gradient(circle at 40% 40%,#ffe04a,#efb10c)"></div>
<div class="produce" role="img" aria-label="Red pepper" style="left:1125px;top:2100px;width:75px;height:75px;border-radius:45% 0 0 45%;background:radial-gradient(#f25a4a,#c81e1e)"></div>

<div class="faq">
  <div class="faq-tab"></div>
  <div class="faq-small">Looking for help?</div>
  <div class="faq-big">Frequently Asked Questions</div>
  <svg class="abs" style="left:665px;top:72px" width="30" height="22" viewBox="0 0 30 22"><path d="M0 11H27M18 2l9 9-9 9" stroke="#fff" stroke-width="2" fill="none"/></svg>
</div>

<footer>
  <div class="foot-brand"><span></span>The Marrow<br>Orchard</div>
  <div class="foot-divider" style="left:343px"></div>
  <div class="foot-divider" style="left:600px"></div>
  <div class="foot-divider" style="left:852px"></div>
  <ul class="foot-links">
    <li>Contact Us</li><li>Terms of Service</li><li>Privacy</li><li>Apps</li><li>Jobs</li><li>For stores</li>
  </ul>
  <ul class="social">
    <li><i></i>Feedspace</li>
    <li><i style="background:#2aa3ef"></i>Chirper</li>
    <li><i style="background:#b83e9e"></i>Snapgrid</li>
    <li><i style="background:#1f4f8a"></i>Workline</li>
  </ul>
  <div class="store" style="top:2932px"><small>GET IT ON</small><b>Play Market</b></div>
  <div class="store" style="top:2988px"><small>GET IT ON</small><b>App Shelf</b></div>
  <div class="chat">
    <svg class="abs" style="left:17px;top:17px" width="26" height="26" viewBox="0 0 26 26"><circle cx="15" cy="11" r="9" fill="none" stroke="#fff" stroke-width="2.5"/><path d="M9 17l-6 6" stroke="#fff" stroke-width="2.5"/></svg>
  </div>
  <div class="to-top">
    <svg class="abs" style="left:13px;top:14px" width="12" height="8" viewBox="0 0 12 8"><path d="M1 7l5-5 5 5" stroke="#fff" stroke-width="2" fill="none"/></svg>
  </div>
  <div class="foot-rule"></div>
  <div class="copyright">Copyright © 2020 - All Rights Reserved.</div>
</footer>

</body>
</html>
```